Breezeway Climate Business Card Design

Design new, 2 sides, business cards for a residential and light commercial heating, air conditioning contractor.

Target Market(s)

Homeowners, small businesses

Industry/Entity Type

Business

Contact Information for Business Card

Dominic Vasquerelli
Phone - 555-214-6837
Email
Address - PO box 618
Millbrook NJ 07999
Website - www.BreezewayClimateLLC.example

Requirements
Must have
• logo, company colors, standard size with no die cut, so I can use printhaven

```html
<!DOCTYPE html>
<html lang="en">
<head>
<meta charset="utf-8">
<title>Breezeway Climate Business Card</title>
<link rel="stylesheet" href="https://fonts.googleapis.com/css2?family=Roboto:wght@400;500;700&display=swap">
<style>
  :root {
    --canvas-bg: #e4e2df;
    --card-dark: #231f20;
    --card-light: #ffffff;
    --brand-red: #9c2230;
    --brand-orange: #f28a24;
    --brand-cream: #fbe8a6;
    --text-grey: #555555;
    --divider: #d4d4d4;
  }
  * { box-sizing: border-box; margin: 0; padding: 0; }
  html, body {
    width: 1200px; height: 1000px; overflow: hidden;
    background: var(--canvas-bg);
    font-family: "Roboto", Arial, sans-serif;
  }
  .canvas { position: relative; width: 1200px; height: 1000px; }
  .card {
    position: absolute; left: 287px; width: 626px; height: 358px;
    box-shadow: 0 6px 18px rgba(0,0,0,0.25);
    overflow: hidden;
  }
  .card-front {
    top: 140px; background: var(--card-dark);
    display: flex; align-items: center; justify-content: center;
  }
  .card-back { top: 531px; background: var(--card-light); }

  .brand-name {
    display: flex; align-items: center; gap: 14px;
    font-weight: 700; white-space: nowrap;
  }
  .brand-mark { border-radius: 50%; flex: none; }
  .card-front .brand-name { font-size: 40px; color: var(--brand-cream); }
  .card-front .brand-mark { width: 30px; height: 30px; background: var(--brand-orange); }

  .back-brand {
    position: absolute; left: 0; top: 0; width: 305px; height: 320px;
    display: flex; align-items: center; justify-content: center;
  }
  .back-brand .brand-name { font-size: 23px; color: var(--brand-red); gap: 9px; }
  .back-brand .brand-mark { width: 18px; height: 18px; background: var(--brand-orange); }

  .divider {
    position: absolute; left: 305px; top: 96px; width: 1px; height: 163px;
    background: var(--divider);
  }
  .contact { position: absolute; left: 333px; top: 100px; color: var(--text-grey); }
  .contact-name {
    font-size: 19px; font-weight: 700; color: var(--brand-red); margin-bottom: 14px;
  }
  .contact-address { font-size: 14.5px; line-height: 18px; margin-bottom: 16px; }
  .contact-list { list-style: none; font-size: 14.5px; }
  .contact-list li { display: flex; align-items: center; gap: 7px; height: 22px; }
  .contact-list svg { width: 11px; height: 11px; flex: none; }

  .footer-bands { position: absolute; left: 0; bottom: 0; width: 626px; height: 24px; }
</style>
</head>
<body>
<main class="canvas">
  <section class="card card-front">
    <div class="brand-name"><span class="brand-mark"></span>Breezeway Climate</div>
  </section>

  <section class="card card-back">
    <div class="back-brand">
      <div class="brand-name"><span class="brand-mark"></span>Breezeway Climate</div>
    </div>
    <div class="divider"></div>
    <div class="contact">
      <p class="contact-name">Dominic Vasquerelli</p>
      <p class="contact-address">PO box 618<br>Millbrook NJ 07999</p>
      <ul class="contact-list">
        <li>
          <svg viewBox="0 0 12 12" aria-hidden="true"><path fill="#f28a24" d="M2.4 0.6 4.2 2.6 3.3 4.1c.7 1.6 2 2.9 3.6 3.6l1.5-.9 2 1.8-1 2c-4.6-.4-8.4-4.2-8.8-8.8z"/></svg>
          555-214-6837
        </li>
        <li>
          <svg viewBox="0 0 12 12" aria-hidden="true"><rect x="0.5" y="2" width="11" height="8" fill="#f28a24"/><path d="M0.5 2.5 6 6.5 11.5 2.5" fill="none" stroke="#fff" stroke-width="1"/></svg>
          info@BreezewayClimateLLC.example
        </li>
        <li>
          <svg viewBox="0 0 12 12" aria-hidden="true"><circle cx="6" cy="6" r="5.2" fill="#f28a24"/><path d="M1 6h10M6 1c-2.2 2.8-2.2 7.2 0 10M6 1c2.2 2.8 2.2 7.2 0 10" fill="none" stroke="#fff" stroke-width="0.8"/></svg>
          www.BreezewayClimateLLC.example
        </li>
      </ul>
    </div>
    <svg class="footer-bands" viewBox="0 0 626 24" aria-hidden="true">
      <rect x="0" y="11" width="300" height="13" fill="#f28a24"/>
      <polygon points="318,0 626,0 626,24 294,24" fill="#9c2230"/>
    </svg>
  </section>
</main>
</body>
</html>
```